New Zealand Export company needs business cards

We need new business cards to match our new logo for a company based in New Zealand who deal specifically with the Pacific Islands. We source, consolidate and ship products out of New Zealand to the Pacific Islands. Will attach our old ones and also new logo.
Would like the Islands we deal with and the areas of work we have access to, to be included on the business cards.

Contact Information for Business Card

T +64 9 571 3048
F +64 9 571 6285
12-18 Kowhai Lane, Drury, 2113
PO Box 814, Drury, Auckland 2247, New Zealand
www.falconfreight.example.nz
E sales@falconfreight.example.nz

Font styles to use
Sans Serif

Colors
85abd2
33a6d7
ffffff

Requirements
Must have
• A company of PWM

```html
<!DOCTYPE html>
<html lang="en">
<head>
<meta charset="utf-8">
<title>Falcon Freight Business Cards</title>
<link href="https://fonts.googleapis.com/css2?family=Open+Sans:wght@300;400;600&display=swap" rel="stylesheet">
<style>
  :root {
    --backdrop: #3b3b39;
    --card: #151617;
    --card-edge: #0c0c0d;
    --sky: #33a6d7;
    --steel: #85abd2;
    --white: #ffffff;
    --soft-white: #e6e8ea;
  }
  * { box-sizing: border-box; margin: 0; padding: 0; }
  html, body {
    width: 1200px; height: 825px; overflow: hidden;
    background: var(--backdrop);
    font-family: "Open Sans", Arial, sans-serif;
  }
  .canvas { position: relative; width: 1200px; height: 825px; }
  .card {
    position: absolute;
    width: 525px; height: 300px;
    background: var(--card);
    border-radius: 6px;
    box-shadow: 0 14px 30px rgba(0,0,0,.45), 0 0 0 1px var(--card-edge);
  }
  .card-front { left: 70px; top: 110px; }
  .card-back { left: 605px; top: 410px; }

  /* front */
  .brand {
    position: absolute; left: 0; right: 0; top: 100px;
    display: flex; align-items: center; justify-content: center; gap: 14px;
  }
  .brand-mark { width: 26px; height: 26px; background: var(--sky); }
  .brand-name {
    font-weight: 600; font-size: 38px; letter-spacing: 3px;
    color: var(--sky); line-height: 1;
  }
  .tagline {
    position: absolute; right: 92px; top: 170px;
    font-size: 12px; color: var(--white); font-weight: 400;
  }

  /* back */
  .person { position: absolute; left: 36px; top: 46px; }
  .person-name {
    font-weight: 300; font-size: 20px; color: var(--white); letter-spacing: .5px;
  }
  .person-title {
    font-size: 11px; color: var(--sky); letter-spacing: .5px; margin-top: 1px;
  }
  .divider {
    position: absolute; left: 112px; right: 22px; top: 106px;
    height: 1.5px; background: var(--sky);
  }
  .brand-small {
    position: absolute; right: 30px; top: 54px;
    display: flex; align-items: center; gap: 8px;
  }
  .brand-small .brand-mark { width: 14px; height: 14px; }
  .brand-small .brand-name { font-size: 20px; letter-spacing: 2px; }
  .contacts {
    position: absolute; left: 36px; top: 132px;
    list-style: none;
  }
  .contacts li {
    display: flex; align-items: center; gap: 10px;
    font-size: 12px; color: var(--soft-white); height: 20px;
  }
  .contacts svg { width: 11px; height: 11px; fill: var(--steel); flex: none; }
  .address {
    position: absolute; right: 24px; bottom: 26px;
    text-align: right; font-size: 13px; line-height: 1.45; color: var(--white);
  }
</style>
</head>
<body>
<main class="canvas">
  <section class="card card-front" aria-label="Card front">
    <div class="brand">
      <span class="brand-mark"></span>
      <span class="brand-name">FALCON FREIGHT</span>
    </div>
    <p class="tagline">A company of PWM</p>
  </section>

  <section class="card card-back" aria-label="Card back">
    <div class="person">
      <p class="person-name">YOUR NAME</p>
      <p class="person-title">JOB TITLE</p>
    </div>
    <div class="divider"></div>
    <div class="brand-small">
      <span class="brand-mark"></span>
      <span class="brand-name">FALCON FREIGHT</span>
    </div>
    <ul class="contacts">
      <li>
        <svg viewBox="0 0 24 24" aria-hidden="true"><path d="M6.6 10.8a15 15 0 0 0 6.6 6.6l2.2-2.2a1 1 0 0 1 1-.25 11.4 11.4 0 0 0 3.6.57 1 1 0 0 1 1 1V20a1 1 0 0 1-1 1A17 17 0 0 1 3 4a1 1 0 0 1 1-1h3.5a1 1 0 0 1 1 1c0 1.25.2 2.45.57 3.57a1 1 0 0 1-.25 1z"/></svg>
        +64 9 571 3048
      </li>
      <li>
        <svg viewBox="0 0 24 24" aria-hidden="true"><path d="M6 2h10v6H6zM3 9h18v9h-3v4H6v-4H3zm5 7v4h8v-4z"/></svg>
        +64 9 571 6285
      </li>
      <li>
        <svg viewBox="0 0 24 24" aria-hidden="true"><path d="M2 5h20v14H2zm2 2v.5l8 5 8-5V7zm0 3v7h16v-7l-8 5z"/></svg>
        sales@falconfreight.example.nz
      </li>
      <li>
        <svg viewBox="0 0 24 24" aria-hidden="true"><path d="M12 2a10 10 0 1 0 0 20 10 10 0 0 0 0-20zm6.9 9h-3a15 15 0 0 0-1.3-6A8 8 0 0 1 18.9 11zM12 4.1c.9 1.3 1.7 3.6 1.9 6.9h-3.8c.2-3.3 1-5.6 1.9-6.9zM9.4 5a15 15 0 0 0-1.3 6h-3A8 8 0 0 1 9.4 5zm-4.3 8h3a15 15 0 0 0 1.3 6 8 8 0 0 1-4.3-6zm6.9 6.9c-.9-1.3-1.7-3.6-1.9-6.9h3.8c-.2 3.3-1 5.6-1.9 6.9zm2.6-.9a15 15 0 0 0 1.3-6h3a8 8 0 0 1-4.3 6z"/></svg>
        www.falconfreight.example.nz
      </li>
    </ul>
    <address class="address" style="font-style:normal">
      12-18 Kowhai Lane, Drury, 2113<br>
      PO Box 814, Drury,<br>
      Auckland 2247, New Zealand
    </address>
  </section>
</main>
</body>
</html>
```